Business Card Design Project - Sports Brand

Brisk is a e-commerce fitness wear brand for ladies who are into gym, pole and swim.

Card should not be overly cluttered and should include the following:

1. logo
2. Name of the company (Use "Brisk Loom Pte Ltd" for now)
3. Address of company (Use a mock address)
4. Representative's name and contact info etc. (use a mock name and contact info)
5. website address

Target Market(s)

Women who are into pole , gym, and swim.

Women who shop online

Industry/Entity Type

E-Commerce

Colors

Designer to choose colors to be used in the design.

Requirements
Nice to have
• feminine sublimation of colours

Need not be printed on traditional paper. We would like the design to be revolutionary and interesting to the eye :)
Should not have
• the design should not be traditional looking. Do not include illustrations of Bikinis, yoga poses etc. in the card.

```html
<!DOCTYPE html>
<html lang="en">
<head>
<meta charset="utf-8">
<title>Brisk Loom – Business Card</title>
<link href="https://fonts.googleapis.com/css2?family=Courier+Prime:wght@400;700&display=swap" rel="stylesheet">
<style>
  :root {
    --bg: #efe9e4;
    --ink: #a8232e;
    --ink-dark: #7a1c24;
    --icon: #333333;
    --white: #ffffff;
    --flow-start: #d8343a;
    --flow-mid: #e8603e;
    --flow-end: #dc78b6;
    --blush-1: #f4c2c8;
    --blush-2: #f7cfcf;
    --blush-3: #f3b8b8;
    --blush-4: #f9dada;
    --lilac: #eec3dc;
  }
  * { box-sizing: border-box; margin: 0; padding: 0; }
  html, body { width: 1200px; height: 960px; overflow: hidden; }
  body { background: var(--bg); position: relative; font-family: "Courier Prime", monospace; }

  .card {
    position: absolute;
    width: 640px;
    height: 366px;
    background: var(--white);
    overflow: hidden;
    box-shadow: 0 6px 18px rgba(60, 30, 20, 0.18);
  }
  .card--front { left: 60px; top: 60px; }
  .card--back { left: 500px; top: 534px; }
  .card__art { position: absolute; inset: 0; width: 100%; height: 100%; }

  .website {
    position: absolute; left: 30px; top: 26px;
    font-size: 25px; color: var(--ink); letter-spacing: 0.5px;
  }
  .social { position: absolute; right: 28px; top: 22px; display: flex; flex-direction: column; gap: 12px; align-items: center; }
  .social__square { width: 40px; height: 40px; background: var(--ink-dark); border-radius: 6px; }
  .social__circle { width: 40px; height: 40px; background: var(--ink-dark); border-radius: 50%; }

  .brand { position: absolute; display: flex; align-items: center; color: var(--ink); font-weight: 400; white-space: nowrap; line-height: 1; }
  .brand__dot { border-radius: 50%; background: var(--ink); flex: none; }

  .brand--front { left: 56px; top: 170px; font-size: 84px; gap: 16px; }
  .brand--front .brand__dot { width: 30px; height: 30px; }

  .brand--back { left: 410px; top: 252px; font-size: 46px; gap: 10px; }
  .brand--back .brand__dot { width: 18px; height: 18px; }

  .contact { position: absolute; left: 26px; top: 40px; color: var(--ink); }
  .contact__name { font-size: 21px; }
  .contact__role { font-size: 16px; margin-top: 2px; }
  .contact__row { display: flex; gap: 10px; align-items: flex-start; margin-top: 20px; }
  .contact__row--tight { margin-top: 4px; }
  .contact__icon { width: 22px; height: 22px; flex: none; margin-top: 2px; }
  .contact__lines { font-size: 17px; line-height: 1.2; }
  .contact__company { font-weight: 700; }
  .contact__phones { margin-top: 44px; }
  .contact__email { position: absolute; left: 26px; bottom: 16px; display: flex; gap: 12px; align-items: center; font-size: 17px; color: var(--ink); }
  .contact__at { color: var(--icon); font-size: 19px; }
</style>
</head>
<body>

  <section class="card card--front">
    <svg class="card__art" viewBox="0 0 640 366">
      <defs>
        <linearGradient id="flow" x1="0" y1="0" x2="1" y2="0">
          <stop offset="0" stop-color="var(--flow-start)"/>
          <stop offset="0.45" stop-color="var(--flow-mid)"/>
          <stop offset="1" stop-color="var(--flow-end)"/>
        </linearGradient>
      </defs>
      <path role="img" aria-label="Soft red-to-pink colour flow decoration" fill="url(#flow)" d="M330,0 C300,60 360,120 430,150 C360,190 360,290 420,366 L640,366 L640,0 Z"/>
    </svg>
    <div class="website">www.briskloom.com</div>
    <div class="social">
      <div class="social__square"></div>
      <div class="social__circle"></div>
    </div>
    <div class="brand brand--front">
      <span class="brand__dot"></span>
      <span class="brand__name">Brisk</span>
    </div>
  </section>

  <section class="card card--back">
    <svg class="card__art" viewBox="0 0 640 366" aria-hidden="true">
      <rect width="640" height="366" fill="var(--blush-2)"/>
      <path fill="var(--lilac)" d="M0,0 L260,0 C200,80 120,140 0,150 Z"/>
      <path fill="var(--blush-1)" d="M260,0 C300,60 380,90 470,80 C540,70 600,40 640,0 Z"/>
      <path fill="var(--blush-3)" opacity="0.6" d="M300,0 C340,50 420,70 500,60 C570,50 610,20 640,0 Z"/>
      <path fill="var(--blush-4)" opacity="0.6" d="M0,220 C120,210 220,260 300,330 L300,366 L0,366 Z"/>
      <path fill="var(--white)" d="M180,366 C280,340 360,300 380,240 C410,150 520,120 640,125 L640,366 Z"/>
      <path fill="var(--white)" d="M0,330 C80,320 160,330 220,366 L0,366 Z"/>
    </svg>

    <div class="contact">
      <div class="contact__name">Mara Vell</div>
      <div class="contact__role">Managing Director</div>

      <div class="contact__row">
        <svg class="contact__icon" viewBox="0 0 22 22" aria-hidden="true">
          <rect x="2" y="5" width="18" height="13" fill="none" stroke="var(--icon)" stroke-width="2"/>
          <path d="M2,5 L11,13 L20,5" fill="none" stroke="var(--icon)" stroke-width="2"/>
        </svg>
        <div class="contact__lines">
          <div class="contact__company">Brisk Loom Pte Ltd</div>
          <div>Suite 12 , 48 Hollin Lane</div>
          <div>Leeds ,England</div>
        </div>
      </div>

      <div class="contact__row contact__phones">
        <svg class="contact__icon" viewBox="0 0 22 22" aria-hidden="true">
          <path d="M3,8 C3,4 19,4 19,8 L16,9 L15,7 L7,7 L6,9 Z" fill="var(--icon)"/>
          <rect x="5" y="11" width="12" height="8" rx="2" fill="var(--icon)"/>
        </svg>
        <div class="contact__lines">
          <div>+44 310 5521 460 Ext 001</div>
          <div>+44 310 5521 400 (Gen)</div>
        </div>
      </div>

      <div class="contact__row contact__row--tight">
        <svg class="contact__icon" viewBox="0 0 22 22" aria-hidden="true">
          <rect x="6" y="2" width="10" height="18" rx="2" fill="none" stroke="var(--icon)" stroke-width="2"/>
          <circle cx="11" cy="16.5" r="1.2" fill="var(--icon)"/>
        </svg>
        <div class="contact__lines">
          <div>+44 712 8830 215</div>
        </div>
      </div>
    </div>

    <div class="contact__email">
      <span class="contact__at">@</span>
      <span>mara.vell@briskloom.com</span>
    </div>

    <div class="brand brand--back">
      <span class="brand__dot"></span>
      <span class="brand__name">Brisk</span>
    </div>
  </section>

</body>
</html>
```